Mini Market Tavo Business Presentation Cards

We need presentation cards with a logo we already own designed at this website as well. We need the printing, delivery and sleek, modem design in harmony with our previous logo design.

Target Market(s)

Low, med and High income class.

Industry/Entity Type

Grocery Store

Contact Information for Business Card

Business logo (Mini Market Tavo), name: Esteban L. Morales/Lidia M. Paz/ Hugo Paz (those are the names for the different cards),
Address: Col. Lomas del Viento, carretera a Tela a 200mts del Centro Comunal. Puerto Cortés, Honduras.
Email: minimarkettavo@correo-ejemplo.hn
Teléfono: (504) 9731-5064

Font styles to use
Serif
Sans Serif

Requirements
Must have
• Business logo (Mini Market Tavo), person name, department,
• Address, phone number, email address.

```html
<!DOCTYPE html>
<html lang="es">
<head>
<meta charset="utf-8">
<title>Mini Market Tavo — Tarjeta de presentación</title>
<link rel="stylesheet" href="https://fonts.googleapis.com/css2?family=Crimson+Text:wght@400;600&display=swap">
<style>
  :root {
    --page-bg: #d8d3cb;
    --card-bg: #eef0ed;
    --card-edge: #c9ccc8;
    --panel-green: #5b9a35;
    --panel-green-dark: #4c8a2b;
    --panel-text: #f3f7ef;
    --name-text: #3f4a3a;
    --brand-red: #b3191d;
    --brand-green: #4f9a2e;
  }
  * { box-sizing: border-box; margin: 0; padding: 0; }
  html, body {
    width: 1200px;
    height: 969px;
    overflow: hidden;
    background: var(--page-bg);
    font-family: "Crimson Text", Georgia, serif;
  }
  .business-card {
    position: absolute;
    left: 120px;
    top: 212px;
    width: 960px;
    height: 545px;
    border-radius: 17px;
    background: var(--card-bg);
    border: 2px solid var(--card-edge);
    box-shadow: 0 10px 30px rgba(0,0,0,0.12);
    overflow: hidden;
  }
  .contact-panel {
    position: absolute;
    left: 0;
    top: 87px;
    width: 483px;
    height: 370px;
    border-radius: 0 20px 20px 0;
    background: linear-gradient(180deg, var(--panel-green), var(--panel-green-dark));
    color: var(--panel-text);
    padding: 30px 0 0 57px;
  }
  .person-name {
    font-size: 31px;
    font-weight: 600;
    line-height: 1.1;
    letter-spacing: 0.3px;
  }
  .person-role {
    font-size: 23px;
    font-weight: 600;
    line-height: 1.3;
    margin-bottom: 26px;
  }
  .address {
    font-size: 21px;
    line-height: 30px;
    font-style: normal;
  }
  .contact-line {
    display: flex;
    align-items: center;
    gap: 16px;
    font-size: 21px;
    line-height: 30px;
  }
  .contact-line.phone { margin-top: 14px; }
  .contact-line.email { margin-top: 4px; }
  .contact-icon { width: 20px; height: 20px; flex: none; }
  .brand-block {
    position: absolute;
    left: 537px;
    top: 218px;
    display: flex;
    align-items: center;
    gap: 22px;
  }
  .brand-name {
    font-size: 36px;
    font-weight: 400;
    line-height: 1;
    color: var(--name-text);
    white-space: nowrap;
  }
  .brand-dot {
    width: 110px;
    height: 110px;
    border-radius: 50%;
    background: var(--brand-green);
  }
  .side-stripe {
    position: absolute;
    right: 0;
    top: 87px;
    width: 19px;
    height: 370px;
    background: var(--brand-red);
    border-radius: 6px 0 0 6px;
  }
</style>
</head>
<body>
  <div class="business-card">
    <section class="contact-panel">
      <h1 class="person-name">Esteban L. Morales</h1>
      <p class="person-role">CEO/Founder</p>
      <address class="address">
        Col. Lomas del Viento,<br>
        carretera a Tela a 200mts<br>
        del Centro Comunal.<br>
        Puerto Cortés, Honduras.
      </address>
      <p class="contact-line phone">
        <svg class="contact-icon" viewBox="0 0 24 24" aria-hidden="true">
          <path fill="currentColor" d="M6.6 10.8a15.1 15.1 0 0 0 6.6 6.6l2.2-2.2c.3-.3.7-.4 1-.2 1.1.4 2.3.6 3.6.6.6 0 1 .4 1 1V20c0 .6-.4 1-1 1A17 17 0 0 1 3 4c0-.6.4-1 1-1h3.5c.6 0 1 .4 1 1 0 1.3.2 2.5.6 3.6.1.3 0 .7-.2 1z"/>
        </svg>
        <span>(504) 9731-5064</span>
      </p>
      <p class="contact-line email">
        <svg class="contact-icon" viewBox="0 0 24 24" aria-hidden="true">
          <path fill="currentColor" d="M2 5h20v14H2z"/>
          <path fill="none" stroke="var(--panel-green)" stroke-width="1.6" d="M3 6.5 12 13l9-6.5"/>
        </svg>
        <span>minimarkettavo@correo-ejemplo.hn</span>
      </p>
    </section>

    <div class="brand-block">
      <p class="brand-name">Mini Market Tavo</p>
      <div class="brand-dot" aria-hidden="true"></div>
    </div>

    <div class="side-stripe" aria-hidden="true"></div>
  </div>
</body>
</html>
```